Online plant nursery needs3 seperate slides for a intro web site slide slide show

We need 3 slide graphics / banners measurments should be 960wide 540 tall and 2mb or smaller. We are an online mail order nursery that focuses sales on Peonies.
Slide 1: Use faded out photos of Peony Garden with many flowers just budding. Our logo and the Words "A Lost Spring is Never Found Again". try to use our logo in a small small watermark on all slides.
Slide 2: Use your own creativity for the slide.... message should say "Free Shipping"
Slide 3: Use your own creativity for the slide .... messgae "Shop Our Other Items". To see site it will be used on go to http://k4830157.tbrwxq9pnlhe.preview82.shopnestle-example.com/

Target Market(s)

home owners age 30 - 65.

Industry/Entity Type

Nursery

Requirements
Must have
• must transition well.
Should not have
• can not be larger than 2MB per file

```html
<!DOCTYPE html>
<html lang="en">
<head>
<meta charset="utf-8">
<title>Petalwood Nursery – A Lost Spring is Never Found Again</title>
<link rel="stylesheet" href="https://fonts.googleapis.com/css2?family=Pinyon+Script&family=Open+Sans:wght@400&family=Cabin:wght@400&display=swap">
<style>
  :root {
    --canvas: #ffffff;
    --blush: #f7d3e6;
    --blush-soft: #fbe6f1;
    --rose: #f2b6d3;
    --petal-core: #f4c4dc;
    --magenta: #d93d8d;
    --magenta-deep: #c92c7c;
    --glow: rgba(255, 255, 255, 0.95);
  }
  * { margin: 0; padding: 0; box-sizing: border-box; }
  html, body {
    width: 1200px;
    height: 675px;
    overflow: hidden;
    background: var(--canvas);
  }
  .slide {
    position: relative;
    width: 1200px;
    height: 675px;
    overflow: hidden;
    background: var(--canvas);
  }
  .swooshes {
    position: absolute;
    inset: 0;
    width: 1200px;
    height: 675px;
  }
  .flower-field {
    position: absolute;
    left: 10px;
    top: 110px;
    width: 1190px;
    height: 480px;
    border-radius: 48% 52% 46% 54% / 50% 46% 54% 50%;
    background:
      radial-gradient(ellipse 20% 34% at 14% 50%, var(--petal-core) 0%, rgba(244,196,220,0.55) 55%, rgba(244,196,220,0) 100%),
      radial-gradient(ellipse 17% 30% at 35% 38%, var(--blush) 0%, rgba(247,211,230,0.5) 60%, rgba(247,211,230,0) 100%),
      radial-gradient(ellipse 18% 32% at 60% 36%, var(--petal-core) 0%, rgba(244,196,220,0.5) 60%, rgba(244,196,220,0) 100%),
      radial-gradient(ellipse 18% 32% at 78% 42%, var(--petal-core) 0%, rgba(244,196,220,0.5) 60%, rgba(244,196,220,0) 100%),
      radial-gradient(ellipse 15% 28% at 72% 75%, var(--blush) 0%, rgba(247,211,230,0.45) 60%, rgba(247,211,230,0) 100%),
      radial-gradient(ellipse 12% 26% at 95% 62%, #fdf7fa 0%, rgba(253,247,250,0) 100%),
      radial-gradient(ellipse 55% 50% at 50% 50%, var(--blush-soft) 0%, rgba(251,230,241,0) 100%);
  }
  .brand {
    position: absolute;
    left: 730px;
    top: 62px;
    display: flex;
    flex-direction: column;
    align-items: flex-start;
  }
  .brand-row {
    display: flex;
    align-items: center;
    gap: 14px;
  }
  .brand-mark {
    width: 44px;
    height: 44px;
    border-radius: 50%;
    background: var(--magenta);
    opacity: 0.85;
  }
  .brand-name {
    font-family: "Open Sans", Arial, sans-serif;
    font-weight: 400;
    font-size: 40px;
    line-height: 1;
    color: var(--magenta);
  }
  .brand-tagline {
    margin-top: 14px;
    margin-left: 58px;
    font-family: "Cabin", Arial, sans-serif;
    font-size: 17px;
    color: var(--magenta);
    letter-spacing: 0.2px;
  }
  .headline {
    position: absolute;
    left: 0;
    top: 360px;
    width: 1200px;
    font-family: "Pinyon Script", cursive;
    font-weight: 400;
    font-size: 78px;
    line-height: 108px;
    color: var(--magenta-deep);
    text-shadow:
      0 0 6px var(--glow),
      0 0 12px var(--glow),
      0 0 18px rgba(255,255,255,0.8);
  }
  .headline-line { display: block; white-space: nowrap; }
  .headline-line--first { padding-left: 240px; }
  .headline-line--second { padding-left: 275px; }
</style>
</head>
<body>
  <main class="slide">
    <svg class="swooshes" viewBox="0 0 1200 675" aria-hidden="true">
      <defs>
        <filter id="soft-blur" x="-20%" y="-50%" width="140%" height="200%">
          <feGaussianBlur stdDeviation="10"/>
        </filter>
        <linearGradient id="band-top" x1="0" y1="0" x2="1" y2="0">
          <stop offset="0" stop-color="#f2b6d3" stop-opacity="0.9"/>
          <stop offset="0.6" stop-color="#f7d3e6" stop-opacity="0.8"/>
          <stop offset="1" stop-color="#ffffff" stop-opacity="0"/>
        </linearGradient>
        <linearGradient id="band-bottom" x1="0" y1="0" x2="1" y2="0">
          <stop offset="0" stop-color="#ffffff" stop-opacity="0"/>
          <stop offset="0.5" stop-color="#f2b6d3" stop-opacity="0.8"/>
          <stop offset="1" stop-color="#f2b6d3" stop-opacity="0.95"/>
        </linearGradient>
      </defs>
      <path d="M-20 150 C 150 60, 330 30, 530 20 L 530 34 C 330 48, 160 90, -20 190 Z" fill="url(#band-top)" filter="url(#soft-blur)"/>
      <path d="M760 660 C 920 620, 1060 600, 1220 560 L 1220 620 C 1060 640, 920 660, 760 675 Z" fill="url(#band-bottom)" filter="url(#soft-blur)"/>
      <path d="M1000 250 C 1080 255, 1150 250, 1220 240 L 1220 280 C 1150 285, 1080 280, 1000 270 Z" fill="#f7d3e6" opacity="0.7" filter="url(#soft-blur)"/>
    </svg>

    <div class="flower-field" role="img" aria-label="Faded photograph of pale pink and white open blossoms with yellow centres spread across the slide"></div>

    <header class="brand">
      <div class="brand-row">
        <span class="brand-mark" aria-hidden="true"></span>
        <span class="brand-name">Petalwood Nursery</span>
      </div>
      <p class="brand-tagline">Beautiful .. Prominent .. Delicate</p>
    </header>

    <h1 class="headline">
      <span class="headline-line headline-line--first">A Lost Spring is</span>
      <span class="headline-line headline-line--second">Never Found Again</span>
    </h1>
  </main>
</body>
</html>
```